KORBALT

The business want a professional looking business card. We have a scetch we will add but want the extra upgrade, and would like more suggestions for variations of our business cards.

```html
<!DOCTYPE html>
<html lang="en">
<head>
<meta charset="utf-8">
<title>KORBALT business cards</title>
<link rel="stylesheet" href="https://fonts.googleapis.com/css2?family=Lato:wght@400;700&family=Playfair+Display:wght@700&display=swap">
<style>
  :root {
    --stage: #8e8e8e;
    --card: #1e1e1e;
    --gold: #c9a14a;
    --gold-light: #f4e78e;
    --gold-deep: #9c6f2e;
    --silver: #d8d8d8;
    --ink: #1a1a1a;
    --white: #f2f2f2;
  }
  * { box-sizing: border-box; margin: 0; padding: 0; }
  html, body { width: 1200px; height: 1200px; overflow: hidden; background: var(--stage); }
  .canvas { position: relative; width: 1200px; height: 1200px; }
  .card {
    position: absolute; left: 281px; width: 641px; height: 366px;
    background: var(--card); border-radius: 22px; overflow: hidden;
  }
  .card-front { top: 195px; }
  .card-back { top: 639px; }
  .wave { position: absolute; inset: 0; width: 100%; height: 100%; }

  .brand { position: absolute; text-align: center; }
  .brand-mark { display: block; margin: 0 auto; border-radius: 50%; background: var(--gold); }
  .brand-name {
    font-family: "Playfair Display", Georgia, serif; font-weight: 700;
    color: var(--gold); letter-spacing: 0.2em; line-height: 1;
  }
  .brand-since {
    font-family: "Lato", Arial, sans-serif; color: var(--white);
    text-transform: uppercase; line-height: 1;
  }

  .front-brand { left: 42px; top: 62px; width: 240px; }
  .front-brand .brand-mark { width: 62px; height: 62px; }
  .front-brand .brand-name { font-size: 34px; margin-top: 38px; padding-left: 0.2em; }
  .front-brand .brand-since { font-size: 11px; letter-spacing: 0.38em; margin-top: 9px; padding-left: 0.38em; }

  .holder { position: absolute; right: 52px; top: 34px; text-align: right; }
  .holder-name {
    font-family: "Playfair Display", Georgia, serif; font-weight: 700;
    font-size: 27px; color: var(--gold); line-height: 1.1;
  }
  .holder-role { font-family: "Lato", Arial, sans-serif; font-size: 16px; color: var(--white); margin-top: 2px; }

  .contact { position: absolute; right: 50px; top: 259px; list-style: none; }
  .contact li {
    display: flex; justify-content: flex-end; align-items: center; gap: 10px;
    font-family: "Lato", Arial, sans-serif; font-size: 14px; color: var(--ink);
    height: 22.5px;
  }
  .contact svg { width: 12px; height: 12px; flex: none; }

  .back-brand { left: 0; right: 0; top: 98px; }
  .back-brand .brand-mark { width: 66px; height: 66px; }
  .back-brand .brand-name { font-size: 46px; margin-top: 42px; padding-left: 0.2em; }
  .brand-family {
    display: flex; align-items: center; justify-content: center; gap: 6px;
    margin-top: 12px; font-family: "Lato", Arial, sans-serif; font-size: 15px;
    color: var(--gold); letter-spacing: 0.85em; text-transform: uppercase;
  }
  .brand-family::before, .brand-family::after {
    content: ""; display: block; width: 48px; height: 1px; background: var(--gold);
  }
  .brand-family span { padding-left: 0.85em; }
  .back-brand .brand-since { font-size: 10px; letter-spacing: 0.8em; margin-top: 14px; padding-left: 0.8em; }
</style>
</head>
<body>
<main class="canvas">

  <section class="card card-front" aria-label="Card front">
    <svg class="wave" viewBox="0 0 802 457" preserveAspectRatio="none" aria-hidden="true">
      <defs>
        <linearGradient id="goldBody" x1="0" y1="0" x2="1" y2="0">
          <stop offset="0" stop-color="#c1952f"/>
          <stop offset="0.38" stop-color="#f6ec95"/>
          <stop offset="0.62" stop-color="#c6a047"/>
          <stop offset="0.8" stop-color="#cfa050"/>
          <stop offset="1" stop-color="#9c6f2e"/>
        </linearGradient>
        <linearGradient id="silverBand" x1="0" y1="0" x2="1" y2="0">
          <stop offset="0" stop-color="#555"/>
          <stop offset="0.45" stop-color="#e6e6e6"/>
          <stop offset="0.75" stop-color="#9a9a9a"/>
          <stop offset="1" stop-color="#4a4a4a"/>
        </linearGradient>
      </defs>
      <path d="M0,392 C140,430 320,445 450,375 C580,305 640,185 802,192 L802,457 L0,457 Z" fill="url(#goldBody)"/>
      <path d="M0,392 C140,430 320,445 450,375 C580,305 640,185 802,192" fill="none" stroke="#1e1e1e" stroke-width="9"/>
      <path d="M60,420 C200,440 360,440 470,360 C580,280 670,190 802,180 L802,170 C680,170 590,250 500,320 C400,400 260,430 60,420 Z" fill="url(#silverBand)"/>
      <path d="M8,364 C130,396 260,402 370,300 C300,380 150,390 8,364 Z" fill="#d9bb4e"/>
      <path d="M560,240 C640,175 720,150 802,158 L802,166 C720,160 650,185 560,240 Z" fill="#3a3a3a"/>
    </svg>

    <div class="brand front-brand">
      <span class="brand-mark" aria-hidden="true"></span>
      <p class="brand-name">KORBALT</p>
      <p class="brand-since">Since 2026</p>
    </div>

    <div class="holder">
      <h1 class="holder-name">Arne Lukas Holmvik</h1>
      <p class="holder-role">CEO &amp; Founder</p>
    </div>

    <ul class="contact">
      <li>004791234567
        <svg viewBox="0 0 24 24"><path fill="#1a1a1a" d="M6.6 10.8c1.4 2.8 3.8 5.1 6.6 6.6l2.2-2.2c.3-.3.7-.4 1-.2 1.1.4 2.3.6 3.6.6.6 0 1 .4 1 1V20c0 .6-.4 1-1 1C10.6 21 3 13.4 3 4c0-.6.4-1 1-1h3.5c.6 0 1 .4 1 1 0 1.3.2 2.5.6 3.6.1.3 0 .7-.2 1L6.6 10.8z"/></svg>
      </li>
      <li>korbalt.llc@mailbox.com
        <svg viewBox="0 0 24 24"><path fill="#1a1a1a" d="M2 5h20v14H2z"/><path fill="none" stroke="#d8b560" stroke-width="1.6" d="M2.5 5.5 12 13l9.5-7.5"/></svg>
      </li>
      <li>www.korbalt.llc
        <svg viewBox="0 0 24 24"><circle cx="12" cy="12" r="10" fill="#1a1a1a"/><path fill="none" stroke="#c9a14a" stroke-width="1.5" d="M2 12h20M12 2c3 3 3 17 0 20M12 2c-3 3-3 17 0 20"/></svg>
      </li>
    </ul>
  </section>

  <section class="card card-back" aria-label="Card back">
    <div class="brand back-brand">
      <span class="brand-mark" aria-hidden="true"></span>
      <p class="brand-name">KORBALT</p>
      <p class="brand-family"><span>Holmvik</span></p>
      <p class="brand-since">Since 2026</p>
    </div>
  </section>

</main>
</body>
</html>
```